Cash Pay Massage Therapy Services for Medical & Therapy Clinics

We are rolling out a new Massage Therapy service in our medical clinics, staffed by licensed professionals. Our offices have a feel between medical clinic and spa. We would like to have some small 8.5x11 posters that let the patients know that we also provide Massages at $80/60 minutes and $50/30 minutes. Typically we always bill insurance but this service would accept cash or credit card.

Target Market(s)

patients that are already having services in our medical offices. Typically, they are already being seen for massage therapy that is billing to their insurance. But, they love their therapist and want to continue to see them when insurance doesnt pay anymore.

Industry/Entity Type

Massage Therapy

Requirements
Must have
• professional (more rehabilitative/less spa) appearance. Prices, logo
Nice to have
• a similar aesthetic to our website.

```html
<!DOCTYPE html>
<html lang="en">
<head>
<meta charset="utf-8">
<title>Calmpoint Massage Pricing Poster</title>
<link href="https://fonts.googleapis.com/css2?family=Jost:wght@300;400&display=swap" rel="stylesheet">
<style>
  :root {
    --backdrop: #eaeaea;
    --ink: #111111;
    --paper: #ffffff;
    --skin-light: #f1d9c8;
    --skin-mid: #d9a68a;
    --skin-deep: #b97c5f;
    --towel: #f4f1ee;
    --disc-light: rgba(255, 255, 255, 0.6);
    --disc-dark: rgba(22, 15, 12, 0.93);
  }
  * { margin: 0; padding: 0; box-sizing: border-box; }
  html, body {
    width: 1200px; height: 1000px; overflow: hidden;
    background: var(--backdrop);
    font-family: "Jost", "Futura", sans-serif;
  }
  .poster {
    position: absolute; left: 388px; top: 159px;
    width: 459px; height: 593px; overflow: hidden;
    background: var(--paper);
  }
  .poster__photo {
    position: absolute; inset: 0;
    background:
      radial-gradient(ellipse 60% 45% at 70% 35%, var(--skin-light), transparent 70%),
      linear-gradient(160deg, #fbf7f4 0%, var(--skin-light) 18%, var(--skin-mid) 55%, var(--skin-deep) 80%, var(--towel) 100%);
  }
  .brand {
    position: absolute; left: 0; top: 0; height: 55px;
    display: flex; align-items: center; gap: 10px;
    padding-right: 12px;
  }
  .brand__square { width: 55px; height: 55px; background: var(--ink); }
  .brand__name {
    font-size: 27px; font-weight: 400; letter-spacing: -0.5px;
    color: var(--ink); line-height: 1;
  }
  .offer-label {
    position: absolute; left: 86px; top: 222px;
    font-size: 17px; font-weight: 400; letter-spacing: -0.3px;
    color: var(--paper);
  }
  .price-disc {
    position: absolute; width: 204px; height: 204px; border-radius: 50%;
  }
  .price-disc--long { left: 41px; top: 262px; background: var(--disc-light); color: var(--ink); }
  .price-disc--short { left: 209px; top: 354px; background: var(--disc-dark); color: var(--paper); }
  .price-disc span { position: absolute; line-height: 1; font-weight: 300; }
  .price__currency { font-size: 26px; }
  .price__amount { font-size: 80px; font-weight: 400 !important; letter-spacing: -3px; }
  .price__minutes { font-size: 46px; letter-spacing: -2px; }
  .price__unit { font-size: 13px; }
  .price__slash { position: absolute; }
</style>
</head>
<body>
  <main class="poster">
    <div class="poster__photo" role="img" aria-label="Photo of a client relaxing with eyes closed while a therapist's hands give a head massage"></div>

    <div class="brand">
      <div class="brand__square"></div>
      <span class="brand__name">calmpoint</span>
    </div>

    <p class="offer-label">MASSAGES AT :</p>

    <div class="price-disc price-disc--long">
      <span class="price__currency" style="left:35px;top:38px;">$</span>
      <span class="price__amount" style="left:57px;top:44px;">80</span>
      <svg class="price__slash" style="left:46px;top:118px;" width="26" height="44" viewBox="0 0 26 44" aria-hidden="true">
        <line x1="18" y1="2" x2="2" y2="42" stroke="currentColor" stroke-width="1.6"/>
        <line x1="25" y1="2" x2="9" y2="42" stroke="currentColor" stroke-width="1.6"/>
      </svg>
      <span class="price__minutes" style="left:67px;top:120px;">60</span>
      <span class="price__unit" style="left:119px;top:143px;">minutes</span>
    </div>

    <div class="price-disc price-disc--short">
      <span class="price__currency" style="left:38px;top:38px;">$</span>
      <span class="price__amount" style="left:52px;top:42px;">50</span>
      <svg class="price__slash" style="left:44px;top:120px;" width="26" height="44" viewBox="0 0 26 44" aria-hidden="true">
        <line x1="18" y1="2" x2="2" y2="42" stroke="currentColor" stroke-width="1.6"/>
        <line x1="25" y1="2" x2="9" y2="42" stroke="currentColor" stroke-width="1.6"/>
      </svg>
      <span class="price__minutes" style="left:64px;top:122px;">30</span>
      <span class="price__unit" style="left:117px;top:145px;">minutes</span>
    </div>
  </main>
</body>
</html>
```